Bref créative
Corwin T. Halbeck D.D.S.
Family Dentistry
Professional
438 W. FM 2296
Suite - B
Alder Springs, OK 74052
corwinthalbeckdds@mailvexo.com
I would like the logo to be designed into this as well as the name of the practice. Which is "Corwin T. Halbeck D.D.S."
This is the side where we write when the patient has a future appointment. usually a space is given to write the date. Followed by a list of the days of the week to indicate that as well as the time of the appointment.
Also incorporate If you must cancel your appointment with us please do so at least 48 hours in advance. Thank you
Please use these logos to design stationary and cards. I like the brushed stroked star for printed materials. The solid version is more for monogramming.

```html
<!DOCTYPE html>
<html lang="en">
<head>
<meta charset="utf-8">
<title>Corwin T. Halbeck D.D.S. — Stationery Set</title>
<link rel="stylesheet" href="https://fonts.googleapis.com/css2?family=Cinzel:wght@400;600&family=Montserrat:wght@400;500&display=swap">
<style>
  :root {
    --brown: #5b2b22;
    --brown-soft: #7a4a40;
    --paper: #ffffff;
    --canvas: #ffffff;
    --frame: #dcdcdc;
    --edge: #d6d2d0;
    --faint: #efe9e6;
    --ink: #6e4a42;
  }
  * { margin: 0; padding: 0; box-sizing: border-box; }
  html, body { width: 1200px; height: 681px; overflow: hidden; background: var(--canvas); }
  body { position: relative; font-family: "Montserrat", sans-serif; color: var(--ink); }

  .presentation-frame {
    position: absolute; left: 14px; top: 14px; width: 1172px; height: 640px;
    border: 1px solid var(--frame);
  }
  .piece {
    position: absolute; background: var(--paper); border: 1px solid var(--edge); overflow: hidden;
  }
  .corner { position: absolute; display: block; }

  .mark { display: block; border-radius: 50%; background: var(--brown); }

  .practice-name {
    font-family: "Cinzel", serif; font-weight: 600; color: var(--brown);
    letter-spacing: 0.02em; white-space: nowrap;
  }
  .practice-tagline {
    font-family: "Cinzel", serif; color: var(--brown-soft);
    letter-spacing: 0.3em; white-space: nowrap;
  }
  .contact { color: var(--brown-soft); white-space: nowrap; line-height: 1.45; }

  /* Envelope front */
  .envelope-front { left: 60px; top: 91px; width: 500px; height: 221px; }
  .envelope-front .mark { position: absolute; left: 62px; top: 18px; width: 30px; height: 30px; }
  .envelope-front .sender { position: absolute; left: 60px; top: 58px; }
  .envelope-front .practice-name { font-size: 15px; }
  .envelope-front .practice-tagline { font-size: 6px; margin: 2px 0 8px 30px; }
  .envelope-front .contact { font-size: 8px; }

  /* Envelope back */
  .envelope-back { left: 60px; top: 348px; width: 500px; height: 240px; }
  .envelope-back .flap { position: absolute; left: 0; top: 0; }
  .envelope-back .monogram {
    position: absolute; left: 0; right: 0; top: 26px;
    display: flex; align-items: center; justify-content: center; gap: 6px;
  }
  .envelope-back .mark { width: 20px; height: 20px; }
  .envelope-back .practice-name { font-size: 11px; }

  /* Letterhead */
  .letterhead { left: 619px; top: 48px; width: 372px; height: 576px; }
  .letterhead .mark { position: absolute; left: 72px; top: 18px; width: 30px; height: 30px; }
  .letterhead .sender { position: absolute; left: 70px; top: 56px; }
  .letterhead .practice-name { font-size: 14px; }
  .letterhead .practice-tagline { font-size: 6px; margin: 2px 0 10px 32px; }
  .letterhead .contact { font-size: 7.5px; }
  .letterhead .watermark {
    position: absolute; left: 268px; top: 408px; width: 150px; height: 150px;
    border-radius: 50%; background: var(--faint);
  }

  /* Business card */
  .business-card { left: 967px; top: 144px; width: 204px; height: 113px; z-index: 2; }
  .business-card .mark { position: absolute; left: 14px; top: 10px; width: 16px; height: 16px; }
  .business-card .sender { position: absolute; left: 12px; top: 30px; }
  .business-card .practice-name { font-size: 8px; }
  .business-card .practice-tagline { font-size: 4px; margin: 1px 0 4px 16px; }
  .business-card .contact { font-size: 4.5px; }

  /* Appointment card */
  .appointment-card { left: 967px; top: 276px; width: 204px; height: 108px; z-index: 2; }
  .appointment-card .card-body { position: absolute; left: 14px; right: 14px; top: 12px; font-size: 5px; color: var(--brown-soft); }
  .appointment-card .title { font-family: "Cinzel", serif; font-size: 6px; letter-spacing: 0.25em; color: var(--brown); margin-bottom: 10px; }
  .appointment-card .weekdays { display: flex; justify-content: space-between; margin-bottom: 10px; }
  .appointment-card .weekdays span::before {
    content: ""; display: inline-block; width: 4px; height: 4px; border: 0.6px solid var(--brown-soft);
    margin-right: 2px; vertical-align: -0.5px;
  }
  .appointment-card .write-in { display: flex; gap: 8px; margin-bottom: 10px; }
  .appointment-card .write-in span { flex: 1; border-bottom: 0.6px solid var(--brown-soft); padding-bottom: 1px; }
  .appointment-card .notice { font-size: 4px; line-height: 1.4; text-align: center; }
</style>
</head>
<body>
  <div class="presentation-frame"></div>

  <!-- Envelope front -->
  <section class="piece envelope-front">
    <span class="mark"></span>
    <div class="sender">
      <div class="practice-name">Corwin T. Halbeck D.D.S.</div>
      <div class="practice-tagline">FAMILY DENTISTRY</div>
      <div class="contact">438 W. FM 2296 | Suite - B<br>Alder Springs, OK 74052</div>
    </div>
    <svg class="corner" style="right:0;top:0" width="64" height="64" viewBox="0 0 64 64">
      <polygon points="0,0 64,0 64,64" fill="var(--brown)"/>
      <line x1="8" y1="0" x2="64" y2="56" stroke="#fff" stroke-width="2"/>
    </svg>
    <svg class="corner" style="left:0;bottom:0" width="60" height="60" viewBox="0 0 60 60">
      <polygon points="0,0 0,60 60,60" fill="var(--brown)"/>
      <line x1="0" y1="8" x2="52" y2="60" stroke="#fff" stroke-width="2"/>
    </svg>
  </section>

  <!-- Envelope back -->
  <section class="piece envelope-back">
    <svg class="flap" width="500" height="240" viewBox="0 0 500 240">
      <polyline points="0,12 250,118 500,12" fill="none" stroke="var(--edge)" stroke-width="1.5"/>
    </svg>
    <div class="monogram">
      <span class="mark"></span>
      <span class="practice-name">Halbeck</span>
    </div>
  </section>

  <!-- Letterhead -->
  <section class="piece letterhead">
    <span class="mark"></span>
    <div class="sender">
      <div class="practice-name">Corwin T. Halbeck D.D.S.</div>
      <div class="practice-tagline">FAMILY DENTISTRY</div>
      <div class="contact">438 W. FM 2296 | Suite - B<br>Alder Springs, OK 74052<br>Phone: 580 555 0142<br>corwinthalbeckdds@mailvexo.com</div>
    </div>
    <div class="watermark"></div>
    <svg class="corner" style="right:0;top:0" width="68" height="68" viewBox="0 0 68 68">
      <polygon points="0,0 68,0 68,68" fill="var(--brown)"/>
      <line x1="8" y1="0" x2="68" y2="60" stroke="#fff" stroke-width="2"/>
    </svg>
    <svg class="corner" style="left:0;bottom:0" width="66" height="66" viewBox="0 0 66 66">
      <polygon points="0,0 0,66 66,66" fill="var(--brown)"/>
      <line x1="0" y1="8" x2="58" y2="66" stroke="#fff" stroke-width="2"/>
    </svg>
  </section>

  <!-- Business card -->
  <section class="piece business-card">
    <svg class="corner" style="left:0;top:0" width="204" height="113" viewBox="0 0 204 113">
      <polygon points="204,8 204,113 40,113" fill="var(--brown)"/>
      <line x1="30" y1="113" x2="204" y2="2" stroke="var(--brown)" stroke-width="1"/>
    </svg>
    <span class="mark"></span>
    <div class="sender">
      <div class="practice-name">Corwin T. Halbeck D.D.S.</div>
      <div class="practice-tagline">FAMILY DENTISTRY</div>
      <div class="contact">438 W. FM 2296 | Suite - B<br>Alder Springs, OK 74052<br>580 555 0142</div>
    </div>
  </section>

  <!-- Appointment card -->
  <section class="piece appointment-card">
    <div class="card-body">
      <div class="title">APPOINTMENT</div>
      <div class="weekdays"><span>Mon</span><span>Tue</span><span>Wed</span><span>Thu</span><span>Fri</span><span>Sat</span></div>
      <div class="write-in"><span>Date</span><span>Time</span></div>
      <p class="notice">If you must cancel your appointment with us please do so<br>at least 48 hours in advance. Thank you</p>
    </div>
  </section>
</body>
</html>
```